Wind Turbine Blade Repair Brochure

Design a new brochure for our relaunched company doing wind turbine blade services. We carry out rotor blade inspections & repairs to wind turbines.Most of the information can be taken from our old brochure but will need new company details, updated images & better design.
New company details are shown in the attached letterhead. Please use the Q8 Harlow Yard address & not the other. Website needs to be: www.fenmoor-lift.uk
Telephone: 020 7958 2316
E-mail: enquiries@fenmoor-lift.com
The other details in the letterhead do not need to be on the brochure
All references to "TOSK" need to change to "Fenmoor Lift"
I have included some additional images that can be used.

Target Market(s)

Wind turbine operators & manufacturers

Requirements
Must have
• All details listed in attached brochure
• Good layout of images
• Eye catching front page design that links well with our logo & industry
Nice to have
• Bar code scan to website / LinkedIn

```html
<!DOCTYPE html>
<html lang="en">
<head>
<meta charset="utf-8">
<title>Fenmoor Lift – Wind Turbine Blade Services Brochure</title>
<link rel="stylesheet" href="https://fonts.googleapis.com/css2?family=Open+Sans:wght@400;600;700;800&display=swap">
<style>
  :root{
    --bg:#e7e8ea;
    --navy:#123f68;
    --navy-deep:#0c2e50;
    --blue:#1f6aa6;
    --sky:#42a8e2;
    --ice:#cfe6f5;
    --ink:#24313f;
    --muted:#5d6874;
    --white:#ffffff;
  }
  *{box-sizing:border-box;margin:0;padding:0}
  html,body{width:1200px;height:2466px;overflow:hidden;background:var(--bg)}
  body{font-family:"Open Sans",Arial,sans-serif;color:var(--ink);position:relative}

  .page{position:absolute;overflow:hidden;background:var(--white);box-shadow:0 8px 24px rgba(0,0,0,.16)}
  .cover{left:320px;top:50px;width:560px;height:792px;--s:1}
  .spread{position:absolute;left:80px;width:1040px;height:735px;box-shadow:0 8px 24px rgba(0,0,0,.16)}
  .spread-outer{top:900px}
  .spread-inner{top:1690px}
  .spread .page{top:0;width:520px;height:735px;box-shadow:none;--s:.93}
  .spread .page.left{left:0}
  .spread .page.right{left:520px}
  .spread .fold{position:absolute;left:519px;top:0;width:2px;height:100%;background:linear-gradient(to right,rgba(0,0,0,.12),rgba(255,255,255,.3));z-index:5}

  .photo{position:absolute;left:0;top:0;width:100%}
  .photo-turbines{height:74%;background:linear-gradient(to bottom,#2f66a6 0%,#7fa6d1 22%,#d7e2ec 40%,#b9cadb 50%,#7f9a5c 58%,#5c7838 72%,#46602a 100%)}
  .photo-technician{height:82%;background:linear-gradient(160deg,#c9d3db 0%,#e9edf0 30%,#9fb2c4 52%,#4b78a8 72%,#6f8a63 88%,#53703c 100%)}
  .swoosh{position:absolute;left:0;top:0;width:100%;height:100%}

  .brand{position:absolute;display:flex;align-items:center;gap:calc(var(--s) * 10px)}
  .brand-dot{width:calc(var(--s) * 26px);height:calc(var(--s) * 26px);border-radius:50%;background:var(--sky)}
  .brand-name{font-weight:700;color:var(--white);font-size:calc(var(--s) * 36px);letter-spacing:.5px;line-height:1}
  .front .brand{left:40%;top:69.5%}
  .back .brand{left:7%;top:84%}
  .back .brand-name{font-size:calc(var(--s) * 28px)}
  .back .brand-dot{width:calc(var(--s) * 20px);height:calc(var(--s) * 20px)}

  .title{position:absolute;left:0;right:6%;top:79%;text-align:right;color:var(--white);font-weight:800;font-size:calc(var(--s) * 23px);letter-spacing:.3px}
  .contact-bar{position:absolute;left:0;width:100%;display:flex;justify-content:space-between;align-items:center;padding:0 6%;background:var(--navy-deep);color:var(--white);font-size:calc(var(--s) * 12.5px);font-weight:600;white-space:nowrap}
  .front .contact-bar{top:86%;height:4.6%}
  .back .contact-bar{top:91%;height:4%;font-size:calc(var(--s) * 11.5px)}
  .contact-bar span{display:flex;align-items:center;gap:6px}
  .contact-bar svg{width:calc(var(--s) * 15px);height:calc(var(--s) * 15px)}
  .address{position:absolute;right:6%;top:92.4%;color:var(--white);font-size:calc(var(--s) * 11.5px);font-weight:600;white-space:nowrap}
  .back .address{left:6%;right:auto;top:95.6%;font-size:calc(var(--s) * 10.5px)}

  /* inner spread */
  .band{position:absolute;left:0;top:0;width:100%;height:100%}
  .tab{position:absolute;left:0;top:28px;width:310px;height:30px;background:linear-gradient(to right,#f2f4f6,#d9dee3);display:flex;align-items:center;padding-left:24px;font-weight:800;font-size:14px;color:var(--navy);clip-path:polygon(0 0,94% 0,100% 100%,0 100%);white-space:nowrap}
  .intro{position:absolute;left:24px;right:26px;top:72px;color:var(--white);font-size:7.6px;line-height:1.45}
  .intro p{margin-bottom:7px}
  .section-head{display:flex;align-items:center;gap:6px;font-weight:800;font-size:11.5px;color:var(--navy);text-transform:uppercase;white-space:nowrap}
  .section-head::before{content:"";flex:0 0 3px;height:12px;background:var(--sky);border-radius:2px}
  .onshore{position:absolute;left:24px;right:26px;top:352px}
  .onshore p{font-size:7.4px;line-height:1.45;color:var(--muted);margin-top:6px}
  .thumbs{position:absolute;left:24px;right:26px;top:440px;display:flex;gap:8px}
  .thumb{flex:1;height:78px}
  .thumb-a{background:linear-gradient(150deg,#3f73a8,#8fb0cf 55%,#5e7b3d)}
  .thumb-b{background:linear-gradient(170deg,#6c9ccc,#c5d6e6 60%,#7d8f6e)}
  .thumb-c{background:linear-gradient(160deg,#dfe6ec,#a9bfd3 50%,#6f8d55)}
  .thumb-d{background:linear-gradient(170deg,#9fbfdc,#e4e9ee 55%,#8a6a55)}
  .inspections{position:absolute;left:24px;right:26px;top:540px}
  .checklist{list-style:none;margin-top:8px}
  .checklist li{font-size:7.4px;color:var(--muted);line-height:1.35;padding-left:12px;position:relative;margin-bottom:2.6px}
  .checklist li::before{content:"";position:absolute;left:0;top:2.5px;width:6px;height:6px;border:1px solid var(--sky);border-radius:1px}
  .repairs{position:absolute;left:24px;top:26px;width:280px;z-index:2}
  .repairs .section-head{color:var(--white);font-size:10.5px}
  .repairs .checklist li{color:var(--ice)}
  .repairs .checklist li::before{border-color:var(--ice)}
  .photo-farm{position:absolute;left:0;top:0;width:100%;height:380px;background:linear-gradient(to bottom,#1d4f86 0%,#3f78b8 30%,#aac4de 52%,#e4ebf1 62%,#7b8d74 70%,#3f6d96 78%,#2d5f8c 100%)}
  .farm-fade{position:absolute;left:0;top:0;width:60%;height:380px;background:linear-gradient(to right,rgba(18,63,104,.92),rgba(18,63,104,.55) 60%,rgba(18,63,104,0))}
  .services{position:absolute;left:22px;right:26px;top:412px;list-style:none}
  .services li{display:flex;gap:10px;margin-bottom:12px}
  .services .icon{flex:0 0 30px;height:30px;border-radius:50%;background:var(--blue);display:flex;align-items:center;justify-content:center}
  .services .icon svg{width:16px;height:16px}
  .services h3{font-size:8.6px;font-weight:700;color:var(--navy);margin-bottom:2px}
  .services p{font-size:7.2px;line-height:1.4;color:var(--muted)}
</style>
</head>
<body>

<!-- Front cover -->
<article class="page cover front">
  <div class="photo photo-turbines" role="img" aria-label="Photograph: wind turbines standing on a grassy hill under a cloudy blue sky"></div>
  <svg class="swoosh" viewBox="0 0 560 792" preserveAspectRatio="none" aria-hidden="true">
    <defs>
      <linearGradient id="coverBlue" x1="0" y1="0" x2="0" y2="1">
        <stop offset="0" stop-color="#1f6aa6"/><stop offset="1" stop-color="#0f3a62"/>
      </linearGradient>
    </defs>
    <path d="M0,498 C170,400 380,360 560,330 L560,792 L0,792 Z" fill="#ffffff"/>
    <path d="M0,512 C170,418 380,380 560,352 L560,792 L0,792 Z" fill="#42a8e2"/>
    <path d="M0,524 C170,434 380,396 560,368 L560,792 L0,792 Z" fill="#e8eef3"/>
    <path d="M0,536 C170,450 380,414 560,388 L560,792 L0,792 Z" fill="url(#coverBlue)"/>
  </svg>
  <div class="brand"><span class="brand-dot"></span><span class="brand-name">Fenmoor Lift</span></div>
  <h1 class="title">WIND TURBINE BLADE SERVICES</h1>
  <div class="contact-bar">
    <span><svg viewBox="0 0 16 16"><circle cx="8" cy="8" r="8" fill="#fff"/><rect x="4" y="5.5" width="8" height="5.5" fill="none" stroke="#123f68" stroke-width="1.2"/><path d="M4,5.5 L8,8.6 L12,5.5" fill="none" stroke="#123f68" stroke-width="1.2"/></svg>enquiries@fenmoor-lift.com</span>
    <span><svg viewBox="0 0 16 16"><circle cx="8" cy="8" r="8" fill="#fff"/><path d="M5.5,4 L7,4 L7.6,6.3 L6.6,7 C7.1,8.2 7.8,8.9 9,9.4 L9.7,8.4 L12,9 L12,10.5 C8,11 5,8 5.5,4 Z" fill="#123f68"/></svg>020 7958 2316</span>
    <span><svg viewBox="0 0 16 16"><circle cx="8" cy="8" r="8" fill="#fff"/><circle cx="8" cy="8" r="4.2" fill="none" stroke="#123f68" stroke-width="1.1"/><path d="M3.8,8 H12.2 M8,3.8 C6,6 6,10 8,12.2 M8,3.8 C10,6 10,10 8,12.2" fill="none" stroke="#123f68" stroke-width=".9"/></svg>www.fenmoor-lift.uk</span>
  </div>
  <p class="address">Unit Q8 Harlow Yard, Brindle Avenue, London, UK E9 4TR</p>
</article>

<!-- Outer spread: back cover + front cover -->
<section class="spread spread-outer">
  <article class="page left back">
    <div class="photo photo-technician" role="img" aria-label="Photograph: rope access technician in red overalls and helmet working on the underside of a turbine blade above a wind farm"></div>
    <svg class="swoosh" viewBox="0 0 560 792" preserveAspectRatio="none" aria-hidden="true">
      <defs>
        <linearGradient id="backBlue" x1="0" y1="0" x2="0" y2="1">
          <stop offset="0" stop-color="#1f6aa6"/><stop offset="1" stop-color="#0f3a62"/>
        </linearGradient>
      </defs>
      <path d="M0,560 C180,640 400,640 560,520 L560,792 L0,792 Z" fill="#ffffff"/>
      <path d="M0,576 C180,656 400,656 560,538 L560,792 L0,792 Z" fill="#42a8e2"/>
      <path d="M0,590 C180,670 400,670 560,556 L560,792 L0,792 Z" fill="#e8eef3"/>
      <path d="M0,604 C180,684 400,684 560,574 L560,792 L0,792 Z" fill="url(#backBlue)"/>
    </svg>
    <div class="brand"><span class="brand-dot"></span><span class="brand-name">Fenmoor Lift</span></div>
    <div class="contact-bar">
      <span><svg viewBox="0 0 16 16"><circle cx="8" cy="8" r="8" fill="#fff"/><rect x="4" y="5.5" width="8" height="5.5" fill="none" stroke="#123f68" stroke-width="1.2"/><path d="M4,5.5 L8,8.6 L12,5.5" fill="none" stroke="#123f68" stroke-width="1.2"/></svg>enquiries@fenmoor-lift.com</span>
      <span><svg viewBox="0 0 16 16"><circle cx="8" cy="8" r="8" fill="#fff"/><path d="M5.5,4 L7,4 L7.6,6.3 L6.6,7 C7.1,8.2 7.8,8.9 9,9.4 L9.7,8.4 L12,9 L12,10.5 C8,11 5,8 5.5,4 Z" fill="#123f68"/></svg>020 7958 2316</span>
      <span><svg viewBox="0 0 16 16"><circle cx="8" cy="8" r="8" fill="#fff"/><circle cx="8" cy="8" r="4.2" fill="none" stroke="#123f68" stroke-width="1.1"/><path d="M3.8,8 H12.2 M8,3.8 C6,6 6,10 8,12.2 M8,3.8 C10,6 10,10 8,12.2" fill="none" stroke="#123f68" stroke-width=".9"/></svg>www.fenmoor-lift.uk</span>
    </div>
    <p class="address">Unit Q8 Harlow Yard, Brindle Avenue, London, UK E9 4TR</p>
  </article>

  <article class="page right front">
    <div class="photo photo-turbines" role="img" aria-label="Photograph: wind turbines standing on a grassy hill under a cloudy blue sky"></div>
    <svg class="swoosh" viewBox="0 0 560 792" preserveAspectRatio="none" aria-hidden="true">
      <defs>
        <linearGradient id="frontBlue" x1="0" y1="0" x2="0" y2="1">
          <stop offset="0" stop-color="#1f6aa6"/><stop offset="1" stop-color="#0f3a62"/>
        </linearGradient>
      </defs>
      <path d="M0,498 C170,400 380,360 560,330 L560,792 L0,792 Z" fill="#ffffff"/>
      <path d="M0,512 C170,418 380,380 560,352 L560,792 L0,792 Z" fill="#42a8e2"/>
      <path d="M0,524 C170,434 380,396 560,368 L560,792 L0,792 Z" fill="#e8eef3"/>
      <path d="M0,536 C170,450 380,414 560,388 L560,792 L0,792 Z" fill="url(#frontBlue)"/>
    </svg>
    <div class="brand"><span class="brand-dot"></span><span class="brand-name">Fenmoor Lift</span></div>
    <h2 class="title">WIND TURBINE BLADE SERVICES</h2>
    <div class="contact-bar">
      <span><svg viewBox="0 0 16 16"><circle cx="8" cy="8" r="8" fill="#fff"/><rect x="4" y="5.5" width="8" height="5.5" fill="none" stroke="#123f68" stroke-width="1.2"/><path d="M4,5.5 L8,8.6 L12,5.5" fill="none" stroke="#123f68" stroke-width="1.2"/></svg>enquiries@fenmoor-lift.com</span>
      <span><svg viewBox="0 0 16 16"><circle cx="8" cy="8" r="8" fill="#fff"/><path d="M5.5,4 L7,4 L7.6,6.3 L6.6,7 C7.1,8.2 7.8,8.9 9,9.4 L9.7,8.4 L12,9 L12,10.5 C8,11 5,8 5.5,4 Z" fill="#123f68"/></svg>020 7958 2316</span>
      <span><svg viewBox="0 0 16 16"><circle cx="8" cy="8" r="8" fill="#fff"/><circle cx="8" cy="8" r="4.2" fill="none" stroke="#123f68" stroke-width="1.1"/><path d="M3.8,8 H12.2 M8,3.8 C6,6 6,10 8,12.2 M8,3.8 C10,6 10,10 8,12.2" fill="none" stroke="#123f68" stroke-width=".9"/></svg>www.fenmoor-lift.uk</span>
    </div>
    <p class="address">Unit Q8 Harlow Yard, Brindle Avenue, London, UK E9 4TR</p>
  </article>
  <div class="fold"></div>
</section>

<!-- Inner spread -->
<section class="spread spread-inner">
  <article class="page left inner">
    <svg class="band" viewBox="0 0 520 735" preserveAspectRatio="none" aria-hidden="true">
      <defs>
        <linearGradient id="innerBand" x1="0" y1="0" x2="1" y2="1">
          <stop offset="0" stop-color="#1f6aa6"/><stop offset="1" stop-color="#0f3a62"/>
        </linearGradient>
      </defs>
      <path d="M0,0 H520 V300 C380,330 200,318 0,290 Z" fill="url(#innerBand)"/>
      <path d="M0,290 C200,318 380,330 520,300 V312 C380,342 200,330 0,302 Z" fill="#42a8e2"/>
      <path d="M0,302 C200,330 380,342 520,312 V318 C380,348 200,336 0,308 Z" fill="#cfe6f5"/>
    </svg>
    <div class="tab">FENMOOR LIFT WIND ACCESS</div>
    <div class="intro">
      <p>Fenmoor Lift Ltd has in excess of 8 years' experience inspecting and repairing rotor blades throughout the UK &amp; Europe combining experience from Aeronautical engineers, boat builders &amp; of course our expert blade specialists.</p>
      <p>Fenmoor Lift has been working as a UK company for more than 10 years according to UK Health and Safety, Environmental &amp; Quality Management requirements. We are using the most advanced rope access techniques and pioneer new developments of a new equipment such as powered rope ascenders, mobile access platforms, etc. providing high cost efficiency and minimizing environmental impact.</p>
      <p>Fenmoor Lift Academy was recently launched in 2015 to help make wind turbine owners and operators aware of the complexity of rotor blade damages, assist them in evaluating rotor blade inspection reports and repair quotations and to supply qualified service technicians for a fast growing wind power industry.</p>
    </div>
    <div class="onshore">
      <h2 class="section-head">Onshore and Offshore Rotor Blade Inspections</h2>
      <p>Exposed glass fibre is not resistant to ultraviolet rays and will begin to absorb water. We work according the Principles for Monitoring the Condition Based Maintenance of Wind Turbines to ensure the delivery of inspection reports to the highest standards. Our inspectors are not only specially trained rope access persons but also qualified rotor blade experts. They work hand in hand with our engineering department to deliver the following services:</p>
    </div>
    <div class="thumbs">
      <div class="thumb thumb-a" role="img" aria-label="Photograph: technician abseiling down a turbine blade"></div>
      <div class="thumb thumb-b" role="img" aria-label="Photograph: technician working on top of a nacelle"></div>
      <div class="thumb thumb-c" role="img" aria-label="Photograph: turbine tower and blades seen from below"></div>
      <div class="thumb thumb-d" role="img" aria-label="Photograph: technician inspecting a blade surface"></div>
    </div>
    <div class="inspections">
      <h2 class="section-head">Rotor Blade &amp; Tower Inspections</h2>
      <ul class="checklist">
        <li>Damage classification in an industry standard scoring system</li>
        <li>Internal rotor blade inspection as a standard part of rotor blade inspection</li>
        <li>Lightning receptor inspections and resistance measurement</li>
        <li>Damage assessment and repair recommendations by experienced engineers</li>
        <li>Management of reports on in-travel service in behalf of our clients</li>
        <li>Tower flange corrosion inspections</li>
        <li>Torque control of tower bolts</li>
        <li>Safety inspection of internal ladder and fall arrest systems</li>
        <li>Inspections of turbine tower surfaces - internal and external</li>
      </ul>
    </div>
  </article>

  <article class="page right inner">
    <div class="photo-farm" role="img" aria-label="Photograph: row of wind turbines beside calm water under a deep blue sky"></div>
    <div class="farm-fade"></div>
    <svg class="band" viewBox="0 0 520 735" preserveAspectRatio="none" aria-hidden="true">
      <path d="M0,350 C160,392 360,392 520,356 V735 H0 Z" fill="#ffffff"/>
      <path d="M0,340 C160,382 360,382 520,346 V356 C360,392 160,392 0,350 Z" fill="#1f6aa6"/>
      <path d="M0,334 C160,376 360,376 520,340 V346 C360,382 160,382 0,340 Z" fill="#42a8e2"/>
    </svg>
    <div class="repairs">
      <h2 class="section-head">Composite Fibre Blade Repairs</h2>
      <ul class="checklist">
        <li>Delamination repairs</li>
        <li>Leading edge protection (Tape &amp; Liquid application)</li>
        <li>Lightning damage repairs</li>
        <li>Warranty repairs</li>
        <li>Installation of Vortex Generators &amp; Gurney flaps</li>
        <li>Root damages</li>
      </ul>
    </div>
    <ul class="services">
      <li>
        <span class="icon"><svg viewBox="0 0 16 16"><path d="M8,2 C10,5.5 12,7.5 12,10 A4,4 0 0 1 4,10 C4,7.5 6,5.5 8,2 Z" fill="#fff"/></svg></span>
        <div><h3>Cleaning of rotor blades and turbine towers</h3><p>We will clean your towers and blades with low impact, biodegradable cleaning agents and experienced operators from pre-saturated cleaning wipes to heavy jet wash equipment, depending on the level of pollution.</p></div>
      </li>
      <li>
        <span class="icon"><svg viewBox="0 0 16 16"><path d="M8,1.5 L13,3.5 V8 C13,11 10.8,13.3 8,14.5 C5.2,13.3 3,11 3,8 V3.5 Z" fill="#fff"/></svg></span>
        <div><h3>Corrosion protection and repairs on wind turbine towers</h3><p>The corrosion process inside the flanges should be prevented since corrosion will attack the tower bolts and in time will result in the bolts complete destruction.</p></div>
      </li>
      <li>
        <span class="icon"><svg viewBox="0 0 16 16"><path d="M3,13 L9.5,6.5" stroke="#fff" stroke-width="2.2" stroke-linecap="round"/><circle cx="11" cy="5" r="3" fill="none" stroke="#fff" stroke-width="1.8"/></svg></span>
        <div><h3>Composite Rotor Blade Repairs</h3><p>Lightning strike damages, open trailing edges, failure of leading edge protection are common damages on rotor blades as is corrosion and hydraulic oil pollution on wind turbine towers.</p></div>
      </li>
      <li>
        <span class="icon"><svg viewBox="0 0 16 16"><path d="M2,10 C4,8 6,8 8,10 C10,12 12,12 14,10" fill="none" stroke="#fff" stroke-width="1.8"/><path d="M8,2 V8 M8,3 L11,5" stroke="#fff" stroke-width="1.4"/></svg></span>
        <div><h3>Offshore and Special Operations</h3><p>Our innovations include the unique environmental tents for on-site repairs reducing costs of blade transportation. Qualified and experienced offshore teams for blade inspection and repairs.</p></div>
      </li>
      <li>
        <span class="icon"><svg viewBox="0 0 16 16"><path d="M3,11 A5,5 0 0 1 13,11 Z" fill="#fff"/><rect x="2" y="11" width="12" height="1.8" fill="#fff"/></svg></span>
        <div><h3>Health and Safety - Target ZERO</h3><p>We at Fenmoor Lift know about the challenge of using rope access methods and are aware of the importance of Health &amp; Safety, Environmental and Quality Management.</p></div>
      </li>
    </ul>
  </article>
  <div class="fold"></div>
</section>

</body>
</html>
```